Riverbend Haven Home Care-Nursing Assessment Form

I am creating a Nursing Assessment Form (which is used to be an intake form for all new patients) for my new home care company, Riverbend Haven Home Care.

It is 15 pages and pretty comprehensive as this is a very regulated field. I have all the necessary content and information attached in the word document below. Now, I am seeking a designer to make it look professional, cohesive and easy to read/ follow.
In order for your Word Document Design to be selected, you must:

1. As mentioned previously, make it easy to read/follow. There should be enough spacing, room to write out all necessary notes, fill out check marks...etc...
2. It should look professional.
3. It should be attractive and eye pleasing. Attached you will find our logo-kindly incorporate it's style into the project as well. The logo should be placed on top of each page.
4. Lastly, we need a Word Document version AND PDF Fillable Option. The fillable PDF should Auto Fill for the Name and Start of Care (SOC) Date.

I have attached a sample form below as well. This is how I envision the finished project to look. Of course, I am open to other suggestions as look as it meets the aforementioned requirements.

Thank you! May the best man or woman win!
Our team looks forward to working with our designer on this project!

Industry/Entity Type

Home Health Care

Font styles to use
Sans Serif

Colors
0255a3
9bcb3c

Requirements
Must have
• Refer to Project Description above.
Nice to have
We must be given a Word Document Option and PDF Fillable Option.

```html
<!DOCTYPE html>
<html lang="en">
<head>
<meta charset="utf-8">
<title>Riverbend Haven Home Care – Initial Assessment Form</title>
<link href="https://fonts.googleapis.com/css2?family=Roboto+Condensed:ital,wght@0,400;0,700;1,400;1,700&display=swap" rel="stylesheet">
<style>
  :root{
    --blue:#0255a3;
    --blue-light:#2a86cf;
    --green:#9bcb3c;
    --line:#a8d5ea;
    --ink:#2b3440;
    --backdrop:#c8d8e5;
    --paper:#ffffff;
  }
  *{box-sizing:border-box;margin:0;padding:0}
  html,body{width:1200px;height:784px;overflow:hidden}
  body{background:var(--backdrop);font-family:"Roboto Condensed",sans-serif;color:var(--ink)}
  .page{
    position:absolute;left:330px;top:8px;width:540px;height:768px;
    background:var(--paper);box-shadow:0 4px 18px rgba(40,70,100,.25);
    overflow:hidden;padding:0 24px 0 26px;
  }
  /* header */
  .accent-top-left{position:absolute;left:0;top:0;width:70px;height:8px;background:var(--green)}
  .accent-top-right{position:absolute;right:0;top:74px;width:46px;height:14px;background:var(--green)}
  .brand{position:absolute;left:0;right:0;top:14px;display:flex;justify-content:center;align-items:center;gap:6px}
  .brand-dot{width:14px;height:14px;border-radius:50%;background:var(--green)}
  .brand-name{font-weight:700;font-size:15px;color:var(--blue);letter-spacing:.3px;text-transform:uppercase}
  .title-band{
    position:absolute;left:70px;right:46px;top:74px;height:14px;
    background:linear-gradient(90deg,var(--blue-light),var(--blue));
    color:#fff;font-size:9px;font-weight:700;letter-spacing:3px;
    display:flex;align-items:center;justify-content:center;text-transform:uppercase;
  }
  .edge-stripe{position:absolute;left:0;top:390px;bottom:0;width:4px;background:var(--blue)}
  .edge-accent{position:absolute;left:8px;top:620px;height:110px;width:4px;background:var(--green)}

  .form{position:absolute;left:26px;right:24px;top:98px;font-size:8.6px}
  .row{display:flex;align-items:flex-end;gap:4px;height:12px;margin-bottom:3.4px}
  .lbl{font-style:italic;white-space:nowrap;line-height:1}
  .head{font-weight:700;font-style:italic;font-size:9.2px;white-space:nowrap;line-height:1}
  .fld{flex:1;height:11px;border:1px solid var(--line)}
  .fld.s{flex:0 0 46px}
  .fld.m{flex:0 0 110px}
  .cb{flex:0 0 9px;width:9px;height:9px;border:1px solid var(--line)}
  .boxes{display:flex;gap:1px}
  .boxes span{width:9px;height:11px;border:1px solid var(--line)}
  .gap{flex:0 0 10px}
  .bullet{width:6px;height:6px;border-radius:50%;background:var(--blue);margin-right:2px;align-self:center}
  .tall{height:22px;margin-bottom:3.4px;display:flex}
  .tall .fld{height:22px}
  .spread{justify-content:space-between}
</style>
</head>
<body>
<main class="page">
  <div class="accent-top-left"></div>
  <header class="brand">
    <span class="brand-dot"></span>
    <span class="brand-name">Riverbend Haven Home Care</span>
  </header>
  <div class="title-band">Initial Assessment Form</div>
  <div class="accent-top-right"></div>
  <div class="edge-stripe"></div>
  <div class="edge-accent"></div>

  <section class="form">
    <div class="row"><span class="lbl">Name</span><span class="fld"></span><span class="lbl">Gender</span><span class="fld s"></span><span class="lbl">MR#</span><span class="fld s"></span><span class="lbl">SOC Date</span><span class="boxes"><span></span><span></span><span></span><span></span><span></span><span></span><span></span><span></span></span></div>
    <div class="row"><span class="lbl">Patient's Name</span><span class="fld"></span></div>
    <div class="row"><span class="lbl">Primary Diagnosis</span><span class="fld"></span><span class="lbl">Secondary Diagnosis</span><span class="fld"></span><span class="lbl">Date</span><span class="boxes"><span></span><span></span><span></span><span></span><span></span><span></span><span></span><span></span></span></div>
    <div class="row"><span class="lbl">Other Pertinent Diagnosis</span><span class="fld"></span><span class="lbl">PCP Name</span><span class="fld"></span></div>
    <div class="row"><span class="lbl">Other Physician Name</span><span class="fld"></span></div>
    <div class="row"><span class="bullet"></span><span class="lbl">Prognosis:</span><span class="gap"></span><span class="lbl">Poor</span><span class="cb"></span><span class="gap"></span><span class="lbl">Fair</span><span class="cb"></span><span class="gap"></span><span class="lbl">Good</span><span class="cb"></span><span class="gap"></span><span class="lbl">Excellent</span><span class="cb"></span></div>
    <div class="row"><span class="lbl">Vital Signs:</span><span class="lbl">Height</span><span class="fld"></span><span class="lbl">Weight</span><span class="fld"></span><span class="lbl">Temp</span><span class="fld"></span><span class="lbl">Pulse</span><span class="fld"></span><span class="lbl">Resp</span><span class="fld"></span><span class="lbl">B/P:</span><span class="fld"></span></div>
    <div class="row"><span class="lbl">Allergies:</span><span class="fld"></span></div>
    <div class="row"><span class="lbl">Past Medical and Surgical History:</span><span class="fld"></span></div>
    <div class="row"><span class="fld"></span></div>

    <div class="row"><span class="head">Support System:</span></div>
    <div class="row"><span class="lbl">Married</span><span class="cb"></span><span class="gap"></span><span class="lbl">Not Married</span><span class="cb"></span><span class="gap"></span><span class="lbl">Single</span><span class="cb"></span><span class="gap"></span><span class="lbl">Divorced</span><span class="cb"></span><span class="gap"></span><span class="lbl">Widowed</span><span class="cb"></span></div>
    <div class="row"><span class="lbl">Lives Alone:</span><span class="lbl">Yes</span><span class="cb"></span><span class="gap"></span><span class="lbl">No</span><span class="cb"></span></div>
    <div class="row"><span class="lbl">Family Composition:</span><span class="fld"></span></div>
    <div class="row"><span class="lbl">Legal Next of Kin:</span><span class="fld"></span></div>
    <div class="row"><span class="lbl">Address:</span><span class="fld"></span><span class="lbl">Email:</span><span class="fld m"></span></div>
    <div class="row"><span class="lbl">Is significant other able, available, capable and willing to care for patient?</span><span class="lbl">Yes</span><span class="cb"></span><span class="gap"></span><span class="lbl">No</span><span class="cb"></span></div>
    <div class="row"><span class="lbl">If No, explain:</span><span class="fld"></span></div>
    <div class="row"><span class="lbl">Educational Needs of Patient/Family:</span><span class="fld"></span></div>

    <div class="row"><span class="head">Environment:</span></div>
    <div class="row"><span class="lbl">Private Home</span><span class="cb"></span><span class="gap"></span><span class="lbl">Apartment</span><span class="cb"></span><span class="gap"></span><span class="lbl">Elevator</span><span class="cb"></span><span class="gap"></span><span class="lbl">Walkup</span><span class="cb"></span></div>
    <div class="row"><span class="head">Safety Hazards in the Home:</span></div>
    <div class="row"><span class="lbl">Sound Structure</span><span class="cb"></span><span class="gap"></span><span class="lbl">Safe Placement of Cords, Rugs and Furniture</span><span class="cb"></span><span class="gap"></span><span class="lbl">Adequate Heating and Ventilation</span><span class="cb"></span><span class="gap"></span><span class="lbl">Adequate Cooking facility</span><span class="cb"></span></div>
    <div class="row"><span class="lbl">Adequate Plumbing/Sanitation/Running Water</span><span class="cb"></span><span class="gap"></span><span class="lbl">Adequate Sleeping Arrangement</span><span class="cb"></span><span class="gap"></span><span class="lbl">Safe Gas/Electric Appliances</span><span class="cb"></span></div>
    <div class="row"><span class="lbl">Grounded Plug for Equipment</span><span class="cb"></span><span class="gap"></span><span class="lbl">Enough Electrical Outlets for Equipment</span><span class="cb"></span><span class="gap"></span><span class="lbl">Working Telephone in the Home</span><span class="cb"></span></div>
    <div class="row"><span class="lbl">Safe storage for Supplies/Equipment/Meds?</span><span class="cb"></span><span class="gap"></span><span class="lbl">Exits Free of Obstruction</span><span class="cb"></span><span class="gap"></span><span class="lbl">Working smoke detectors?</span><span class="cb"></span><span class="gap"></span><span class="lbl">Fire extinguisher in home?</span><span class="cb"></span></div>
    <div class="row"><span class="lbl">Infestations of pests?</span><span class="cb"></span><span class="gap"></span><span class="lbl">Neighborhood safe?</span><span class="cb"></span></div>
    <div class="row"><span class="head">Comments:</span><span class="fld"></span></div>
    <div class="row"><span class="fld"></span></div>

    <div class="row"><span class="head">Caregiver's Contact Information:</span></div>
    <div class="row"><span class="lbl">Name:</span><span class="fld"></span><span class="lbl">Telephone</span><span class="fld m"></span></div>
    <div class="row"><span class="lbl">Address:</span><span class="fld"></span><span class="lbl">Email:</span><span class="fld m"></span></div>
    <div class="row"><span class="lbl">Days/Time Available:</span><span class="fld"></span></div>
    <div class="row"><span class="head">Caregivers Ability to Assist Patient / Able to Provide:</span></div>
    <div class="row"><span class="lbl">Personal Care:</span><span class="lbl">Yes</span><span class="cb"></span><span class="lbl">No</span><span class="cb"></span><span class="gap"></span><span class="lbl">Mobility:</span><span class="lbl">Yes</span><span class="cb"></span><span class="lbl">No</span><span class="cb"></span><span class="gap"></span><span class="lbl">Prepare/Serve Meals:</span><span class="lbl">Yes</span><span class="cb"></span><span class="lbl">No</span><span class="cb"></span></div>
    <div class="row"><span class="lbl">Maintain Safe/Clean Environment</span><span class="lbl">Yes</span><span class="cb"></span><span class="lbl">No</span><span class="cb"></span><span class="gap"></span><span class="lbl">Perform/ Assist with Procedures</span><span class="lbl">Yes</span><span class="cb"></span><span class="lbl">No</span><span class="cb"></span></div>
  </section>
</main>
</body>
</html>
```